Custom unique Stationary design for Logistics company

We need a custom, unique , elegant and luxurious full stationary design using our new logo, following these guidelines:
1- Business card: double sided, both sides uses the navy blue as the background main color (same as the code of the navy blue used in our logo).
2- envelope and folder: also use the same navy blue as the main background color.
3- book cover( notepad cover) : same thing with the navy blue
4- letterhead: feel free to use the combination of the colors in our logo.
5- rest of the items are up to your creativity

Target Market(s)

corporates and other businesses

Industry/Entity Type

Logistics and heavy machines contractors

Requirements
Must have
• Letterhead, business card, envelope, notepad cover, paper, file
Nice to have
• navy blue to be main background color for business card, envelope, notepad cover

```html
<!DOCTYPE html>
<html lang="en">
<head>
<meta charset="utf-8">
<title>KVR Envelope Set</title>
<link rel="stylesheet" href="https://fonts.googleapis.com/css2?family=Montserrat:wght@500;700&display=swap">
<style>
  :root {
    --canvas-grey: #a9a9a9;
    --navy: #1b5172;
    --navy-deep: #134763;
    --navy-flap: #225b7c;
    --orange: #e1602a;
    --paper-white: #eceef0;
    --text-white: #ffffff;
  }
  * { box-sizing: border-box; margin: 0; padding: 0; }
  html, body { width: 1200px; height: 900px; overflow: hidden; }
  body {
    background: radial-gradient(circle at 50% 40%, #c2c2c2, var(--canvas-grey));
    font-family: "Montserrat", sans-serif;
    position: relative;
  }

  /* Envelope back with open flap */
  .envelope-back {
    position: absolute;
    left: 70px;
    top: 240px;
    width: 600px;
    height: 430px;
  }
  .envelope-back .flap {
    position: relative;
    width: 600px;
    height: 130px;
  }
  .envelope-back .flap svg {
    display: block;
    width: 600px;
    height: 130px;
  }
  .flap-brand {
    position: absolute;
    left: 0;
    top: 28px;
    width: 600px;
    display: flex;
    justify-content: center;
    transform: rotate(180deg);
  }
  .envelope-back .body {
    position: relative;
    width: 600px;
    height: 300px;
    background: var(--navy);
  }

  .brand {
    display: inline-flex;
    flex-direction: column;
    color: var(--text-white);
  }
  .brand-row { display: flex; align-items: center; gap: 8px; }
  .brand-name {
    font-weight: 700;
    font-size: 44px;
    letter-spacing: 1px;
    line-height: 1;
    color: var(--text-white);
  }
  .brand-dot {
    width: 10px; height: 10px; border-radius: 50%;
    background: var(--orange);
  }
  .brand-tagline {
    font-weight: 500;
    font-size: 6px;
    letter-spacing: 0.6px;
    margin-top: 4px;
    text-transform: uppercase;
    color: var(--text-white);
  }

  .back-brand { position: absolute; left: 48px; top: 40px; }

  .contact-list {
    position: absolute;
    left: 48px;
    top: 170px;
    list-style: none;
    color: var(--text-white);
    font-weight: 500;
    font-size: 14px;
    line-height: 19px;
  }
  .contact-list li { display: flex; align-items: center; gap: 8px; }
  .contact-list svg { width: 11px; height: 11px; flex: none; }

  .base-band {
    position: absolute;
    left: 0; bottom: 42px;
    width: 600px; height: 14px;
    background: var(--paper-white);
  }

  /* Envelope front, standing portrait */
  .envelope-front {
    position: absolute;
    left: 770px;
    top: 110px;
    width: 320px;
    height: 640px;
    background: var(--navy-deep);
    box-shadow: 0 20px 40px rgba(0,0,0,0.25);
  }
  .front-brand { position: absolute; right: 60px; top: 110px; }
  .front-stripe {
    position: absolute;
    right: 24px; top: 0;
    width: 16px; height: 640px;
  }
</style>
</head>
<body>

  <section class="envelope-back" aria-label="Envelope back">
    <div class="flap">
      <svg viewBox="0 0 600 130" preserveAspectRatio="none" aria-hidden="true">
        <path d="M0 130 L20 0 L580 0 L600 130 Z" fill="var(--navy-flap)"/>
      </svg>
      <div class="flap-brand">
        <div class="brand">
          <div class="brand-row"><span class="brand-name">KVR</span><span class="brand-dot"></span></div>
        </div>
      </div>
    </div>
    <div class="body">
      <div class="brand back-brand">
        <div class="brand-row"><span class="brand-name">KVR</span><span class="brand-dot"></span></div>
        <span class="brand-tagline">Heavy machine logistics contractors</span>
      </div>

      <ul class="contact-list">
        <li>
          <svg viewBox="0 0 12 12"><path d="M2 1 L4.5 1 L5 4 L3.6 5 A6 6 0 0 0 7 8.4 L8 7 L11 7.5 L11 10 A9 9 0 0 1 2 1 Z" fill="var(--orange)"/></svg>
          +000 000 0000
        </li>
        <li>
          <svg viewBox="0 0 12 12"><rect x="1" y="2.5" width="10" height="7" fill="var(--orange)"/><path d="M1 2.5 L6 6.5 L11 2.5" stroke="var(--navy)" fill="none"/></svg>
          info@kvrfreight.com
        </li>
        <li>
          <svg viewBox="0 0 12 12"><circle cx="6" cy="6" r="5" fill="var(--orange)"/><path d="M1 6 H11 M6 1 V11" stroke="var(--navy)" stroke-width="0.8"/></svg>
          www.webname.com
        </li>
      </ul>

      <div class="base-band"></div>
    </div>
  </section>

  <section class="envelope-front" aria-label="Envelope front">
    <div class="brand front-brand">
      <div class="brand-row"><span class="brand-name">KVR</span><span class="brand-dot"></span></div>
      <span class="brand-tagline">Heavy machine logistics contractors</span>
    </div>
    <svg class="front-stripe" viewBox="0 0 16 640" aria-hidden="true">
      <path d="M2 0 H14 V290 L8 300 H2 Z" fill="var(--paper-white)"/>
      <path d="M4 312 L12 306 M4 322 L12 316" stroke="var(--orange)" stroke-width="3"/>
      <path d="M8 340 L14 330 V640 H2 V340 Z" fill="var(--paper-white)"/>
    </svg>
  </section>

</body>
</html>
```